create clean, simple business card template

using the logo created now we need to create a simple, elegant business card design to suit

Industry/Entity Type

Business

Font styles to use
Other font styles liked:
• segoe ui

Requirements
Must have
• Front:
"Name:"
"Title:"
"Mobile:"
"email:"
and the logo

Back:
Logo
Nice to have
• Text in black but other graphics etc to match colours in logo as provided

```html
<!DOCTYPE html>
<html lang="en">
<head>
<meta charset="utf-8">
<title>Kestrel Homes – Business Cards</title>
<link rel="stylesheet" href="https://fonts.googleapis.com/css2?family=Open+Sans:wght@400;600;700&display=swap">
<style>
  :root {
    --page-bg: #e9e6e1;
    --card-bg: #ffffff;
    --brand-gold: #9a7a3c;
    --brand-dark: #3b2f26;
    --text-dark: #1a1a1a;
    --card-shadow: rgba(40, 30, 20, 0.18);
  }
  * { box-sizing: border-box; margin: 0; padding: 0; }
  html, body {
    width: 1200px;
    height: 704px;
    overflow: hidden;
    background: var(--page-bg);
    font-family: "Open Sans", "Segoe UI", sans-serif;
  }
  .card-sheet {
    width: 1200px;
    height: 704px;
    display: flex;
    align-items: center;
    justify-content: center;
    gap: 60px;
  }
  .business-card {
    width: 500px;
    height: 286px;
    background: var(--card-bg);
    box-shadow: 0 6px 18px var(--card-shadow);
    display: flex;
    align-items: center;
    justify-content: center;
  }
  .brand-lockup {
    display: flex;
    align-items: center;
    gap: 14px;
  }
  .brand-dot {
    width: 34px;
    height: 34px;
    border-radius: 50%;
    background: var(--brand-dark);
  }
  .brand-divider {
    width: 1px;
    align-self: stretch;
    background: var(--brand-gold);
  }
  .brand-name {
    color: var(--brand-gold);
    font-weight: 600;
    font-size: 30px;
    letter-spacing: 0.5px;
    white-space: nowrap;
  }
  .card-back .brand-lockup { height: 44px; }
  .card-front {
    justify-content: flex-start;
    padding-left: 34px;
    gap: 14px;
  }
  .card-front .brand-dot { width: 30px; height: 30px; }
  .card-front .brand-name { font-size: 24px; }
  .front-divider {
    width: 1.5px;
    height: 150px;
    background: var(--brand-gold);
  }
  .contact-block {
    color: var(--text-dark);
    font-size: 13.5px;
    line-height: 1.35;
  }
  .contact-name {
    font-weight: 700;
    font-size: 15px;
  }
</style>
</head>
<body>
  <main class="card-sheet">
    <section class="business-card card-back" aria-label="Card back">
      <div class="brand-lockup">
        <span class="brand-dot"></span>
        <span class="brand-divider"></span>
        <span class="brand-name">Kestrel Homes</span>
      </div>
    </section>

    <section class="business-card card-front" aria-label="Card front">
      <div class="brand-lockup">
        <span class="brand-dot"></span>
        <span class="brand-name">Kestrel Homes</span>
      </div>
      <span class="front-divider"></span>
      <div class="contact-block">
        <p class="contact-name">Alex Morgan</p>
        <p class="contact-title">CEO</p>
        <p class="contact-phone">555-014-2368</p>
        <p class="contact-email">alexmorgan@mail.com</p>
      </div>
    </section>
  </main>
</body>
</html>
```